Single Page Real estate project Flyer

We need a single page (front and back) real estate project flyer for our EB-5 immigration investment business. The final design should communicate a well structured investment project destined for success and providing stability and financial safety. I provided some other project materials as reference and a old flyer we tried to design ourselves.

Target Market(s)

Wealthy immigrant investors who wish to immigrate to the United States through investment into this real estate project

Industry/Entity Type

Real Estate Development

Font styles to use
Serif

Colors
0455a3
3276b5
ec1f27

Requirements
Must have
• luxury and high end design appealing to wealthy real estate investors who happen to be international (Indian, Chinese, Brazilian and Vietnamese are core markets).
• Luxury look is a must, simple delivery, its a simple take-away flier designed to just be a giant business card so it doesnt need to sell the story alone all by itself. Just be attractive enough to get an email or call back.
Nice to have
• how to integrate the project renderings with the in progress construction photos.

```html
<!DOCTYPE html>
<html lang="en">
<head>
<meta charset="utf-8">
<title>The Scholar — EB-5 Project Flyer</title>
<link href="https://fonts.googleapis.com/css2?family=Cinzel:wght@500&family=Marcellus&family=Crimson+Text:wght@400;600&family=Montserrat:wght@400;600&display=swap" rel="stylesheet">
<style>
  :root{
    --stage:#8f9092;
    --paper:#f4f4f3;
    --paper-shade:#e9e9e8;
    --gold:#c9a44c;
    --gold-deep:#a9852f;
    --gold-band:#dcc278;
    --slate:#53565a;
    --ink:#3b3b3b;
    --logo-gray:#5c5e61;
    --blue-deep:#1f3f8f;
    --blue:#3563b0;
    --sunset:#e8a89a;
  }
  *{margin:0;padding:0;box-sizing:border-box}
  html,body{width:1200px;height:960px;overflow:hidden}
  body{background:var(--stage);position:relative;font-family:"Crimson Text",Georgia,serif;color:var(--ink)}
  .page{position:absolute;top:114px;width:506px;height:716px;
    background:linear-gradient(135deg,var(--paper) 0%,var(--paper-shade) 50%,var(--paper) 100%);overflow:hidden}
  .page--front{left:80px}
  .page--back{left:618px}

  .brand{position:absolute;display:flex;align-items:center;gap:8px;
    font-family:"Cinzel",serif;font-weight:500;color:var(--logo-gray)}
  .brand__square{width:22px;height:22px;background:var(--logo-gray)}
  .brand--front{left:48px;top:46px;font-size:19px;letter-spacing:.5px}
  .brand--back{left:0;right:0;top:586px;justify-content:center;font-size:22px;letter-spacing:1px}

  .hero{position:absolute;left:27px;top:102px;width:453px;height:584px}
  .hero__render{position:absolute;inset:0 0 59px 0;
    background:linear-gradient(180deg,var(--blue-deep) 0%,var(--blue) 45%,#6b86c0 70%,var(--sunset) 86%,#3d4a4a 100%)}
  .hero__title{position:absolute;left:33px;width:172px;top:24px;text-align:center;color:#fff}
  .bracket{display:block;margin:0 auto;width:24px;height:10px;border:3px solid var(--gold)}
  .bracket--top{border-bottom:none}
  .bracket--bottom{border-top:none}
  .hero__the{font-family:"Marcellus",serif;font-size:19px;letter-spacing:1px;margin-top:14px;line-height:1}
  .hero__name{font-family:"Marcellus",serif;font-size:29px;letter-spacing:2px;line-height:1.15}
  .hero__rule{width:172px;height:1px;background:rgba(255,255,255,.8);margin:8px 0 12px}
  .hero__sub{font-family:"Montserrat",sans-serif;font-size:10px;letter-spacing:2px;line-height:17px;margin-bottom:14px}
  .hero__band{position:absolute;left:0;right:0;bottom:0;height:59px;background:var(--slate);
    text-align:center;padding-top:16px}
  .hero__place{font-family:"Montserrat",sans-serif;font-weight:600;font-size:10.5px;letter-spacing:.8px;color:var(--gold)}
  .hero__note{font-family:"Montserrat",sans-serif;font-style:italic;font-size:8.5px;color:var(--gold);margin-top:5px}

  .ribbon{position:absolute;right:0;top:0}
  .section-mark{position:absolute;left:0;right:0;text-align:center}
  .heading{position:absolute;left:0;right:0;text-align:center;font-family:"Marcellus",serif;
    font-size:16px;letter-spacing:.5px;color:var(--gold-deep);font-weight:400}
  .tagline{position:absolute;left:0;right:0;top:96px;text-align:center;font-family:"Crimson Text",serif;font-size:10px;letter-spacing:.3px}
  .seals{position:absolute;top:118px;left:58px;display:flex;gap:18px}
  .seal{width:64px;height:64px;border-radius:50%;
    background:radial-gradient(circle at 40% 35%,#f1d88a 0%,var(--gold) 35%,#7a5c1c 70%,#3a2c10 100%);
    border:3px solid var(--gold)}
  .list{position:absolute;left:0;right:0;list-style:none;text-align:center;font-size:11.8px;line-height:15.4px;color:var(--ink)}
  .list li::before{content:"\25C6";color:var(--gold);font-size:9px;margin-right:4px;vertical-align:1px}
  .list li.cont::before{content:none}
  .divider{position:absolute;left:188px;width:131px;top:282px;height:1px;background:#6a6a6a}
  .photo{position:absolute;top:326px;width:155px;height:92px}
  .photo--site{left:94px;background:linear-gradient(180deg,#5e8fc9 0%,#9bb7d6 35%,#7a7a72 60%,#4b4a45 100%)}
  .photo--aerial{left:258px;background:linear-gradient(180deg,#8e9aa6 0%,#6f8a98 40%,#4fb2cf 55%,#7a7f78 100%)}
  .caption{position:absolute;top:424px;width:170px;text-align:center;font-size:7.5px;color:#555}
  .caption--site{left:86px}
  .caption--aerial{left:250px}
  .jobs{position:absolute;left:67px;width:375px;top:532px;height:16px;background:var(--gold-band);
    display:flex;justify-content:center;align-items:center;font-size:8px;color:#4a4030;white-space:nowrap}
  .jobs span+span{border-left:1px solid #fff;padding-left:5px;margin-left:5px}
  .contact{position:absolute;left:150px;top:619px;width:208px;height:97px;background:var(--slate);text-align:center;color:#fff}
  .contact__label{font-family:"Montserrat",sans-serif;font-size:7px;letter-spacing:1px;margin-top:12px}
  .contact__phone{font-family:"Montserrat",sans-serif;font-size:17px;color:var(--gold);margin-top:6px;letter-spacing:.5px}
  .contact__mail{font-family:"Montserrat",sans-serif;font-size:7.2px;color:var(--gold);letter-spacing:.8px;margin-top:2px}
  .contact__web{font-family:"Montserrat",sans-serif;font-size:7.5px;color:var(--gold);letter-spacing:2px;margin-top:11px}
</style>
</head>
<body>

<section class="page page--front" aria-label="Flyer front">
  <div class="brand brand--front"><span class="brand__square"></span>Harwell Regional Center</div>

  <div class="hero">
    <div class="hero__render" role="img" aria-label="Architectural rendering of a 19-story glass residential tower at dusk, street with trees and cars in front"></div>
    <div class="hero__title">
      <span class="bracket bracket--top"></span>
      <p class="hero__the">THE</p>
      <p class="hero__name">SCHOLAR</p>
      <div class="hero__rule"></div>
      <p class="hero__sub">SILICON VALLEY<br>STUDENT HOUSING</p>
      <span class="bracket bracket--bottom"></span>
    </div>
    <div class="hero__band">
      <p class="hero__place">DOWNTOWN SAN JOSE, SILICON VALLEY, CALIFORNIA</p>
      <p class="hero__note">468 Ft Away From Valley State University's Front Gate</p>
    </div>
  </div>
</section>

<section class="page page--back" aria-label="Flyer back">
  <svg class="ribbon" width="200" height="120" viewBox="0 0 200 120" aria-label="100% Approval History">
    <polygon points="0,0 90,0 200,63 200,116" fill="var(--gold-band)"/>
    <text transform="translate(134.5,41.2) rotate(30)" text-anchor="middle" dominant-baseline="middle" font-family="Crimson Text, serif" font-size="13" font-weight="600" fill="#4a3d1e">100%</text>
    <text transform="translate(126,56) rotate(30)" text-anchor="middle" dominant-baseline="middle" font-family="Marcellus, serif" font-size="12" fill="#4a3d1e" letter-spacing=".4">APPROVAL HISTORY</text>
  </svg>

  <div class="section-mark" style="top:44px"><span class="bracket bracket--top"></span></div>
  <h2 class="heading" style="top:70px">INVESTMENT HIGHLIGHTS</h2>
  <p class="tagline">RARE EB-5 INVESTMENT OPPORTUNITY IN THE HEART OF SILICON VALLEY</p>

  <div class="seals" aria-label="Guarantee seals">
    <div class="seal"></div><div class="seal"></div><div class="seal"></div><div class="seal"></div><div class="seal"></div>
  </div>

  <ul class="list" style="top:192px">
    <li>Loan Style Investment</li>
    <li>$28.5 Million Offering (57 Investors)</li>
    <li>I-526 Money-Back Guarantee</li>
    <li>Construction Completion Guarantee</li>
    <li>100% Equity Pledge</li>
  </ul>
  <div class="divider"></div>

  <h2 class="heading" style="top:300px">PROJECT HIGHLIGHTS</h2>
  <div class="photo photo--site" role="img" aria-label="Construction photo of the concrete tower frame with a crane"></div>
  <div class="photo photo--aerial" role="img" aria-label="Aerial view of downtown with the university campus highlighted next to the tower"></div>
  <p class="caption caption--site">Expected Completion: Year 2020</p>
  <p class="caption caption--aerial">Close Proximity to Valley State University</p>

  <ul class="list" style="top:447px">
    <li>19 Story Residential Tower</li>
    <li>469 feet from Valley State University</li>
    <li>260 Apartments (1000+ Beds)</li>
    <li>Club style amenities including Pool,</li>
    <li class="cont">Student Lounge, Gym, Tech Lab, Bike parking, Cafe and more</li>
  </ul>

  <div class="jobs">
    <span>Over 1042+ Jobs already created</span>
    <span>Only 570 needed</span>
    <span>100% of USCIS Jobs Requirement Complete</span>
  </div>

  <div class="section-mark" style="top:562px"><span class="bracket bracket--bottom"></span></div>
  <div class="brand brand--back"><span class="brand__square"></span>Calloway</div>

  <div class="contact">
    <p class="contact__label">PLEASE CONTACT US AT</p>
    <p class="contact__phone">+1(925) 555-0184</p>
    <p class="contact__mail">info@callowaygroup.com</p>
    <p class="contact__web">WWW.CALLOWAYGROUP.COM</p>
  </div>
</section>

</body>
</html>
```